International business needs a web page design

We need a web page design for a new service that our new "sub-company" of our existing company will offer. We are based in Denmark, and our new "sub-company" is called 'Velkari'. The service we offer is automated server configuration and In-Depth monitoring, and optional operations support. Our monitoring has a lot of graphs (like those seen here: https://velkari.example/ with either black or white background ) and the website needs to communicate a sense of Security/safety and that our customers can relax, because we have the full overview of their service and servers. The website should not be with black background.

We deliver low price, high quality and professional operations - which we can do, because we automate it and have people with 15+ years of experience doing so.

We have attached :
a file with our logo : velkari
a file showing the content of the frontage : frontpage
a file showing the content of the user page(for logged in users) : User page
a file showing the pop-up dialog "page" : CallToAction_route
a file showing the 3-steps for the frontpage : 3-step for frontpage

Target Market(s)

Chief Technological officers (CTO's) and Developers (small business, run by developers) - who needs professional IT operations.

Industry/Entity Type

Business

Coding

Coded - Design and coding required

Number of Pages Required

3 page

Requirements
Must have
• Frontpage :
• A lot of visualization(some with people too) rather than a lot of text
• A short, describing text on front page telling what people get
• 3 steps showing people how it works. (Could be presented in a video placed on top of a big front image or perhaps with all 3 steps/pictures shown at the same time or perhaps in a completely different way).
Nice to have
• A big front image(perhaps a person with a cellphone showing graphs and a "all okay" message) with a text and the 3-steps pictures/or video on top of it
• 3 boxes under the front image/top of the site showing what benefits people get from the service
Should not have
• Not a black/dark site

```html
<!DOCTYPE html>
<html lang="en">
<head>
<meta charset="utf-8">
<title>Velkari – Instant server setup &amp; In-depth monitoring</title>
<link href="https://fonts.googleapis.com/css2?family=Roboto:wght@400;500&family=Roboto+Condensed:wght@400;500;700&display=swap" rel="stylesheet">
<style>
  :root {
    --brand: #1a9dd9;
    --ink: #1d1d1d;
    --body: #444444;
    --rule: #d9d9d9;
    --band: #efefef;
    --footer: #231f20;
    --white: #ffffff;
    --hero-a: #5d6a63;
    --hero-b: #c9b7a6;
    --hero-c: #8f2f33;
  }
  * { margin: 0; padding: 0; box-sizing: border-box; }
  html, body { width: 932px; height: 1200px; overflow: hidden; background: var(--white); }
  body { position: relative; font-family: "Roboto", Arial, sans-serif; color: var(--body); }

  .site-header { position: absolute; left: 0; top: 0; width: 932px; height: 80px; background: var(--white); }
  .brand-dot { position: absolute; left: 79px; top: 14px; width: 51px; height: 51px; border-radius: 50%; background: var(--brand); }
  .brand-name { position: absolute; left: 138px; top: 13px; font-family: "Roboto", Arial, sans-serif; font-weight: 500; font-size: 34px; line-height: 36px; color: var(--ink); letter-spacing: -0.5px; white-space: nowrap; }
  .brand-tagline { position: absolute; left: 140px; top: 50px; font-family: "Roboto Condensed", Arial, sans-serif; font-weight: 500; font-size: 9px; line-height: 10px; color: var(--ink); white-space: nowrap; }
  .main-nav { position: absolute; right: 80px; top: 26px; display: flex; align-items: center; }
  .main-nav a { font-family: "Roboto Condensed", Arial, sans-serif; font-size: 12px; font-weight: 500; color: var(--ink); text-decoration: none; margin-left: 31px; }
  .main-nav .login { background: var(--brand); color: var(--white); width: 66px; height: 29px; display: flex; align-items: center; justify-content: center; margin-left: 25px; }

  .hero { position: absolute; left: 0; top: 80px; width: 932px; height: 494px; overflow: hidden; }
  .hero-photo { position: absolute; inset: 0; background: linear-gradient(110deg, var(--hero-a) 0%, #8a8f86 30%, var(--hero-b) 52%, var(--hero-c) 72%, #3b3f45 100%); }
  .hero-caption { position: absolute; left: 80px; top: 238px; width: 358px; min-height: 99px; background: rgba(30, 30, 30, 0.72); padding: 12px 20px; font-family: "Roboto Condensed", Arial, sans-serif; font-size: 16px; line-height: 22.5px; color: var(--white); white-space: nowrap; }
  .hero-dots { position: absolute; left: 80px; top: 458px; display: flex; gap: 3px; }
  .hero-dots span { width: 11px; height: 11px; border-radius: 50%; background: var(--white); }
  .hero-dots span.active { background: transparent; border: 2px solid var(--white); }
  .hero-cta { position: absolute; left: 637px; top: 395px; width: 215px; height: 55px; background: var(--brand); color: var(--white); font-family: "Roboto Condensed", Arial, sans-serif; font-weight: 500; font-size: 13px; line-height: 17.5px; text-align: center; display: flex; align-items: center; justify-content: center; text-decoration: none; }

  .steps { position: absolute; left: 0; top: 574px; width: 932px; height: 290px; }
  .step { position: absolute; top: 20px; height: 251px; text-align: center; }
  .step + .step { border-left: 1px solid var(--rule); }
  .step-label { font-size: 15px; color: var(--ink); margin-top: 12px; }
  .step-icon { width: 74px; height: 74px; border-radius: 50%; background: var(--brand); margin: 16px auto 0; display: flex; align-items: center; justify-content: center; }
  .step-title { font-size: 13px; font-weight: 500; color: var(--brand); margin-top: 20px; }
  .step-text { font-size: 10px; line-height: 14.4px; color: var(--body); margin: 4px auto 0; }

  .benefits { position: absolute; left: 0; top: 858px; width: 932px; height: 255px; }
  .benefits-bg { position: absolute; inset: 0; }
  .benefit { position: absolute; top: 35px; height: 183px; text-align: center; }
  .benefit + .benefit { border-left: 1px solid var(--rule); }
  .benefit-icon { height: 38px; display: flex; align-items: center; justify-content: center; margin-top: 4px; }
  .benefit-title { font-size: 13px; font-weight: 500; color: var(--brand); margin-top: 14px; line-height: 14.5px; }
  .benefit-text { font-size: 10px; line-height: 16px; color: var(--body); margin: 4px auto 0; }

  .site-footer { position: absolute; left: 0; top: 1113px; width: 932px; height: 87px; background: var(--footer); color: var(--white); font-size: 10.5px; }
  .connect { position: absolute; left: 79px; top: 21px; }
  .social { position: absolute; left: 79px; top: 40px; display: flex; gap: 4px; }
  .social span { width: 18px; height: 18px; border-radius: 2px; }
  .footer-links { position: absolute; right: 80px; top: 21px; }
  .footer-links a { color: var(--white); text-decoration: none; }
  .copyright { position: absolute; right: 80px; top: 44px; }
</style>
</head>
<body>

<header class="site-header">
  <span class="brand-dot"></span>
  <span class="brand-name">Velkari</span>
  <div class="brand-tagline">Instant server setup &amp; In-depth monitoring</div>
  <nav class="main-nav">
    <a href="#">SERVICES</a>
    <a href="#">ABOUT US</a>
    <a href="#" class="login">LOGIN</a>
  </nav>
</header>

<section class="hero">
  <div class="hero-photo" role="img" aria-label="Smiling man in a red checked shirt sitting in a car, holding out a phone showing an all-ok tick"></div>
  <p class="hero-caption">Lorem Ipsum is simply dummy text of the printing<br>and typesetting industry. Lorem Ipsum has been<br>the industry's standard dummy text ever since</p>
  <div class="hero-dots"><span></span><span></span><span class="active"></span><span></span><span></span></div>
  <a href="#" class="hero-cta">CLICK TO GET<br>INSTANT SERVER SETUP NOW</a>
</section>

<section class="steps">
  <div class="step" style="left:48px;width:238px;">
    <div class="step-label">STEP 1</div>
    <div class="step-icon">
      <svg width="34" height="36" viewBox="0 0 34 36"><circle cx="17" cy="9" r="8" fill="#fff"/><path d="M2 35 V28 Q2 20 10 20 H24 Q32 20 32 28 V35 Z" fill="#fff"/></svg>
    </div>
    <div class="step-title">CHOOSE PROFILE IMAGE</div>
    <p class="step-text" style="width:190px;font-size:10.5px;line-height:17.5px;">(SEE THAT SECTION IN<br>"CALL TO ACTION" ROUTE)</p>
  </div>
  <div class="step" style="left:286px;width:297px;">
    <div class="step-label">STEP 2</div>
    <div class="step-icon">
      <svg width="44" height="32" viewBox="0 0 44 32" fill="none" stroke="#fff" stroke-width="3.5" stroke-linecap="round" stroke-linejoin="round"><path d="M12 6 L3 16 L12 26"/><path d="M32 6 L41 16 L32 26"/><path d="M25 3 L19 29"/></svg>
    </div>
    <div class="step-title">RUN COMMAND</div>
    <p class="step-text" style="width:240px;">(User copy pastes command from velkari.example page, into their server (into the console indow-typicly window with black background and white text). Perhaps visualized with the velkari.example user page (see user page) and a console window and some arrows showing "copynpaste" action</p>
  </div>
  <div class="step" style="left:583px;width:293px;">
    <div class="step-label">STEP 3</div>
    <div class="step-icon">
      <svg width="44" height="44" viewBox="0 0 44 44"><circle cx="22" cy="22" r="20" fill="#fff"/><path d="M13 22 L20 29 L31 16" fill="none" stroke="var(--brand)" stroke-width="5" stroke-linecap="round" stroke-linejoin="round"/></svg>
    </div>
    <div class="step-title">DONE</div>
    <p class="step-text" style="width:228px;">Server is ready and they can now start using their server for its purpose. Perhaps show some of the graph images from velkari.example in one box(performance graphs as atitle) and that monitoring works in another box with a cellphone showing "all Ok"</p>
  </div>
</section>

<section class="benefits">
  <svg class="benefits-bg" width="932" height="255" viewBox="0 0 932 255" aria-hidden="true"><path d="M0 2 L932 26 L932 255 L0 255 Z" fill="var(--band)"/></svg>
  <div class="benefit" style="left:48px;width:279px;">
    <div class="benefit-icon">
      <svg width="35" height="35" viewBox="0 0 35 35" fill="none" stroke="var(--brand)" stroke-width="3.5"><circle cx="17.5" cy="17.5" r="15"/><path d="M17.5 9 V18.5 H11" stroke-linecap="round"/></svg>
    </div>
    <div class="benefit-title">IT'S FAST AND EASY</div>
    <p class="benefit-text" style="width:225px;">We have done all the hard work, so you can focus on what you need out of your server - your server will be ready in a few minutes... (instant Server Setup)</p>
  </div>
  <div class="benefit" style="left:327px;width:283px;">
    <div class="benefit-icon">
      <svg width="36" height="32" viewBox="0 0 36 32"><rect x="1" y="1" width="34" height="23" rx="2" fill="var(--brand)"/><rect x="4" y="4" width="28" height="15" fill="#fff"/><rect x="14" y="24" width="8" height="5" fill="var(--brand)"/><rect x="9" y="28" width="18" height="3" fill="var(--brand)"/></svg>
    </div>
    <div class="benefit-title">RELAX AND REST ASSURED</div>
    <p class="benefit-text" style="width:225px;">We will monitor your server and are ready 24/7 to handle issues on your server - so you do not have to be the systems expert. We will advise and help yout to ensure that you can grow with your success, and handle any emergency.</p>
  </div>
  <div class="benefit" style="left:610px;width:266px;">
    <div class="benefit-icon">
      <svg width="38" height="30" viewBox="0 0 38 30" fill="none" stroke="var(--brand)" stroke-width="3" stroke-linejoin="round"><path d="M2 1 V28 H37"/><path d="M6 23 L14 14 L20 19 L32 7"/><path d="M25 6 H33 V14" stroke-linecap="round"/></svg>
    </div>
    <div class="benefit-title">YOU WILL LOVE YOUR DETAILED<br>PERFORMANCE GRAPHS</div>
    <p class="benefit-text" style="width:216px;">We will tell you, minute by minute how your website performs and how close your server is to its limits, so you can reach in time.</p>
  </div>
</section>

<footer class="site-footer">
  <div class="connect">CONNECT WTIH US</div>
  <div class="social" aria-label="Social links">
    <span style="background:#3b5998"></span>
    <span style="background:#2fa9e0"></span>
    <span style="background:#1a7bb9"></span>
    <span style="background:#f7931e"></span>
  </div>
  <div class="footer-links"><a href="#">HOME</a> &nbsp;|&nbsp; <a href="#">SERVICES</a> &nbsp;|&nbsp; <a href="#">CONTACT US</a></div>
  <div class="copyright">COPYRIGHTS @ 2014 ALL RIGHTS RESERVED</div>
</footer>

</body>
</html>
```